Create a Brochure Design for Harlow Senior Living

Harlow Senior Living is a subsidiary of the Harlow Care Group. This brochure is specifically for the Harlow Senior Living company and brand. Create a 3 panel, front and back, tri-fold brochure. This brochure will be a way to introduce our senior living care home to the community, prospective, clients, and various referral partners. It is modern and state of the art home. Like the home, the brochure must be eye catching, unique in its deliverables (as it doesn’t feel like a care facility) and demonstrate both attention to detail and comfort. Our organization is sophisticated and built around warmth, care and individualized personal attention. The most important aspect of this design is to focus on creating a nurturing, warm, and inviting feel where you would want to put your own loved ones in our care home.
I am open to the creativity of the designer to develop something based on the above criteria; however I would like the design to work well with the existing collateral material. What I mean by that is that while I want everything to have its own personality and stand out as its own brand representative, I still need to be able to tell that the overall design concept stays stylistically inside of the same ‘family’ of existing designed material. Because of this, below I would like for the designer to pull inspiration from the link to our website (Located below) as well as from the attachment of our recently refreshed business cards (Attached). This should allow each design to be unique and creative, while still staying inside of a framework and the feel/style that I am looking for.
Finally, I want all the designers to understand that this brochure design is for a facility where we are responsible to provide care for active, positive, and happy seniors/elders. We have care professionals and staff on-site to provide 24x7, around the clock, care to the elders and geriatric residents as it is needed and required. The photos that are used must represent aging gracefully and with elegance.
Target Market(s)
Seniors(50+), Caring Family Members, Social Workers, Physicians, Hospitals
Industry/Entity Type
Business
Requirements
Must have
- • The company logo must be included.
Nice to have
- Attached you will find a sampling of images related to the long term care industry. Please feel free to use your own images as you see fit. The interior care home pictures are of our actual facility and should be incorporated into the brochure and your design.
Company Information
• Look under the Harlow Senior Living tab at
www.harlowcaregroup.example.

```html
<!DOCTYPE html>
<html lang="en">
<head>
<meta charset="utf-8">
<title>Harlow Senior Living – Tri-fold Brochure</title>
<link href="https://fonts.googleapis.com/css2?family=Crimson+Text:wght@400;600&family=Italianno&display=swap" rel="stylesheet">
<style>
  :root {
    --teal: #82cdb9;
    --teal-deep: #5fb7a2;
    --teal-soft: #a9dccd;
    --slate: #6e7479;
    --slate-dark: #5c6166;
    --ink: #3c3f42;
    --heading-teal: #4fae99;
    --paper: #ffffff;
    --canvas: #ffffff;
    --rule: #cccccc;
  }
  * { box-sizing: border-box; margin: 0; padding: 0; }
  html, body { width: 1200px; height: 1000px; overflow: hidden; background: var(--canvas); }
  body { position: relative; font-family: "Crimson Text", Georgia, serif; color: var(--ink); }
  .abs { position: absolute; }

  .sheet-label { position: absolute; font-family: "Italianno", cursive; font-size: 44px; color: #111; line-height: 1; letter-spacing: 2px; }

  .sheet { position: absolute; left: 242px; width: 676px; background: var(--paper); }
  .sheet-outside { top: 57px; height: 441px; border-top: 1px solid #999; border-right: 1px solid var(--rule); }
  .sheet-inside { top: 523px; height: 439px; }

  .photo { position: absolute; }
  .band-teal { background: var(--teal); }

  .script { font-family: "Italianno", cursive; color: #fff; line-height: 1; letter-spacing: 1px; white-space: nowrap; }

  .quote { position: absolute; left: 0; top: 91px; width: 225px; height: 74px; background: var(--slate); color: #fff; font-size: 8.4px; line-height: 1.3; padding: 4px 4px 0 4px; text-align: justify; letter-spacing: -0.05px; z-index: 2; }
  .quote .signature { font-family: "Italianno", cursive; font-size: 14px; line-height: 1; white-space: nowrap; }

  .contact { position: absolute; left: 0; top: 383px; width: 225px; text-align: center; color: var(--slate-dark); font-size: 11px; line-height: 1.25; }

  .panel-rule { position: absolute; left: 225px; top: 0; width: 1px; height: 441px; background: var(--rule); }

  .address-band { left: 225px; top: 143px; width: 225px; height: 28px; background: linear-gradient(90deg, var(--teal), rgba(130,205,185,0.35)); color: #fff; font-size: 10.5px; line-height: 1.2; padding: 2px 5px; }

  .directions { left: 231px; top: 178px; width: 215px; font-size: 9.2px; line-height: 1.3; color: var(--ink); }
  .directions h3 { font-weight: 400; font-size: 12px; color: var(--heading-teal); margin-top: 7px; line-height: 1.2; }
  .directions h3:first-child { margin-top: 0; }

  .brand-name { font-family: "Crimson Text", Georgia, serif; font-weight: 400; color: var(--slate); text-align: center; line-height: 1.05; }
  .brand-mark { width: 14px; height: 14px; background: var(--teal); margin: 0 auto 6px; }

  .cover-tagline { left: 450px; top: 293px; width: 226px; height: 60px; background: var(--slate); }
  .cover-tagline .line-one { position: absolute; left: 10px; top: 8px; font-size: 23px; }
  .cover-tagline .line-two { position: absolute; left: 38px; top: 28px; font-size: 29px; }

  .inside-header { left: 0; top: 30px; width: 506px; height: 47px; background: var(--slate); }
  .inside-header .line-one { position: absolute; left: 16px; top: 2px; font-size: 26px; }
  .inside-header .line-two { position: absolute; left: 120px; top: 20px; font-size: 30px; }

  .inside-logo { left: 506px; top: 30px; width: 117px; height: 47px; background: var(--paper); padding-top: 6px; }

  .features { left: 450px; top: 77px; width: 226px; height: 243px; background: var(--teal); color: #fff; padding: 3px 6px 0 6px; }
  .features h3 { font-weight: 400; font-size: 11.5px; line-height: 1.2; border-bottom: 1px solid rgba(255,255,255,0.8); width: 150px; margin-top: 3px; }
  .features p { font-size: 8.6px; line-height: 1.2; text-align: justify; }
  .features ul { list-style: none; font-size: 8.4px; line-height: 1.28; }
  .feature-lists { display: flex; gap: 6px; margin-top: 7px; }
  .feature-lists ul { width: 100px; }
  .feature-lists li::before { content: "• "; }

  .photo-caption { position: absolute; right: 8px; bottom: 4px; font-size: 26px; }
</style>
</head>
<body>

  <div class="sheet-label" style="left:478px; top:16px;">Back Cover</div>
  <div class="sheet-label" style="left:22px; top:472px;">Inside Flap</div>
  <div class="sheet-label" style="left:934px; top:472px;">Cover Page</div>
  <div class="sheet-label" style="left:924px; top:937px;">Inside Flyer</div>

  <section class="sheet sheet-outside">
    <div class="photo band-teal" style="left:0; top:0; width:225px; height:91px;" role="img" aria-label="Teal band with faint script lettering texture"></div>
    <blockquote class="quote">“Harlow Care strives to create a home-like atmosphere where you and your loved ones can feel secure. The warm, well-trained staff works closely with the residents to provide the utmost care and comfort. The lush green environment offers a real natural environment full of love and peace.” <span class="signature">-Mara Ellison</span></blockquote>
    <div class="photo" style="left:0; top:165px; width:225px; height:215px; background:linear-gradient(160deg,#e9dcae 0%,#a8703f 45%,#5a2e22 80%,#3a2219 100%);" role="img" aria-label="Photo of the home's dining room with wooden table and chairs, pendant lamps and red curtains"></div>
    <div class="contact">
      808-555-0142<br>
      www.harlowcare.example<br>
      48 Lanakila Bay Dr, Kailua,<br>
      Honolulu, Hawaii 96734, USA
    </div>
    <div class="panel-rule"></div>

    <div class="photo" style="left:226px; top:0; width:224px; height:143px; background:linear-gradient(135deg,#e6e8e4 0%,#eef0ec 40%,#cfe6c4 60%,#e6e8e4 100%);" role="img" aria-label="Street map of the Aikahi area in Kailua with a marker at the home's location"></div>
    <div class="abs address-band">48 Lanakila Bay Dr, Kailua,<br>Honolulu, Hawaii 96734, USA</div>
    <div class="abs directions">
      <h3>If you’re coming from Town (Honolulu)</h3>
      Take the Pali Highway to Kailua.<br>
      After the tunnel, on the Windward side,<br>
      take a left on HI-83N/Kamehameha Highway.<br>
      Merge onto H3 via the ramp to Kailua/Kaneohe MCBH.<br>
      Follow signs for Kailua.<br>
      Turn left on Kaneohe Bay Drive.<br>
      We’re a half-mile ahead on your right.
      <h3>If you’re coming from Kailua</h3>
      Head down N. Kalaheo Drive toward Kaneohe.<br>
      Cross Mokapu Blvd<br>
      (the Aikahi Market will be on your right).<br>
      Drive past the next stoplight.<br>
      Our Home is a block or two ahead, on your left.
      <h3>If you’re coming from Kaneohe</h3>
      Head west toward H-830N.<br>
      Make a U-Turn at Kapalai Road.<br>
      Take a left turn onto Kaneohe Bay Drive.<br>
      You can either stay on Kaneohe Bay Drive until<br>
      you reach our Home which will be on your right.
    </div>

    <div class="abs" style="left:450px; top:110px; width:226px;">
      <div class="brand-mark"></div>
      <div class="brand-name" style="font-size:34px;">Harlow<br>Senior Living</div>
    </div>
    <div class="abs cover-tagline">
      <span class="script line-one">Someone you can depend on...</span>
      <span class="script line-two">Without Question.</span>
    </div>
    <div class="photo band-teal" style="left:450px; top:353px; width:226px; height:88px;" role="img" aria-label="Teal band with faint script lettering texture"></div>
  </section>

  <section class="sheet sheet-inside">
    <div class="photo band-teal" style="left:0; top:0; width:225px; height:30px; opacity:0.8;" role="img" aria-label="Teal band with faint script lettering texture"></div>
    <div class="abs inside-header">
      <span class="script line-one">Just bring your suitcase</span>
      <span class="script line-two">We’ll take care of the rest.</span>
    </div>
    <div class="abs inside-logo">
      <div class="brand-name" style="font-size:17px;">Harlow<br>Senior Living</div>
    </div>

    <div class="photo" style="left:0; top:77px; width:450px; height:243px; background:linear-gradient(180deg,#f3ecd4 0%,#e4d3a5 35%,#9a7a58 65%,#6b5a48 100%);" role="img" aria-label="Photo of the bright living room with a large leather sectional sofa, rug and windows">
      <span class="script photo-caption">Enrich your lifestyle.</span>
    </div>

    <div class="abs features">
      <h3>Welcome Home</h3>
      <p>Our beautiful Kailua home is situated in the Aikahi Area with 19 fully furnished private rooms with private bathrooms, community areas, dining room and specially dedicated activity rooms.</p>
      <h3>Daily Life</h3>
      <p>In our home, neighbors can do a little gardening, stay in touch with family and friends, relax at the spa, take up a new hobby, outings, exercise programs, beach walks, group outings, movie nights &amp; more.</p>
      <h3>Personal Care</h3>
      <p>Maintain purpose in life while having personal care assistance as needed. From daily bathing, dressing, grooming to excersise, meals and medication. Everything is taken care of, 24/7.</p>
      <div class="feature-lists">
        <ul>
          <li>3 daily meals + snacks</li>
          <li>Activities</li>
          <li>Laundry</li>
          <li>Housekeeping</li>
          <li>Utilities</li>
          <li>Accommodations</li>
        </ul>
        <ul>
          <li>Medication Management</li>
          <li>Care Planning</li>
          <li>Regular Nursing Visits</li>
          <li>Access to Staff 24/7</li>
          <li>Lifestyle Support</li>
          <li>Regular nursing visits</li>
        </ul>
      </div>
    </div>

    <div class="photo" style="left:0; top:320px; width:225px; height:119px; background:linear-gradient(160deg,#e8d69a 0%,#b89466 50%,#5a3d2a 100%);" role="img" aria-label="Photo of a private bedroom with a made bed and balcony doors"></div>
    <div class="photo" style="left:225px; top:320px; width:225px; height:119px; background:linear-gradient(180deg,#eef0ee 0%,#d8dcd8 55%,#a99a80 100%);" role="img" aria-label="Photo of an accessible private bathroom with walk-in shower"></div>
    <div class="photo" style="left:450px; top:320px; width:226px; height:119px; background:linear-gradient(160deg,#efe6b8 0%,#c9a87a 50%,#6e4a30 100%);" role="img" aria-label="Photo of a sitting room with sofa and game table"></div>
  </section>

</body>
</html>
```